LUMINARA VENTURES NAMECARD

Need to design a name card with an existing logo.

As we are professional corporate services provider our name card has to project a professional image.
Should be corporate, simple & professional.

Our corporate color is maroon red but not too dull.

Please refer to our website at www.luminaraventures.com.sg

Would attach our logo herewith.

Front surface of namecard details:
LUMINARA VENTURES PTE LTD
Registration No. 208711845K

Tan Wei Ling CA (Singapore)
Director

Tel +65 6481 2957
Mobile +65 9172 3086
tan@luminaraventures.com.sg
www.luminaraventures.com.sg

47 Plover Lane
#07-12 Harbourlight Plaza
Singapore 276351

Back of namecard:-
OUR CORE SERVICES
Incorporation services
Corporate Secretarial Services
Accountancy service
Goods & Services Taxation
Corporate & Personal Taxation
Financial Reporting
Payroll Administration

AFFILIATES:
BRIGHTWAVE CORPORATE SERVICES PTE LTD
PINNACLEFORMATIONSPTE LTD
LIM MANAGEMENT SERVICES PTE LTD
RW HO AND COMPANY PTE LTD
LEDGERLY ACADEMY

```html
<!DOCTYPE html>
<html lang="en">
<head>
<meta charset="utf-8">
<title>Luminara Ventures Name Card</title>
<link href="https://fonts.googleapis.com/css2?family=Source+Sans+3:wght@400;600&display=swap" rel="stylesheet">
<style>
  :root {
    --backdrop: #a9a8ad;
    --maroon: #cf2239;
    --maroon-deep: #a5162a;
    --ink-red: #c8203a;
    --paper: #fbfbfb;
    --white: #ffffff;
  }
  * { margin: 0; padding: 0; box-sizing: border-box; }
  html, body {
    width: 1200px; height: 863px; overflow: hidden;
    background: var(--backdrop);
    font-family: "Source Sans 3", Arial, sans-serif;
  }
  .stage { position: relative; width: 1200px; height: 863px; }
  .card {
    position: absolute; left: 300px; width: 600px; height: 360px;
    box-shadow: 0 6px 18px rgba(0,0,0,0.25);
  }
  .card-back { top: 55px; background: var(--maroon); color: var(--white); }
  .card-front { top: 448px; background: var(--paper); color: var(--ink-red); }

  .wordmark {
    position: absolute; text-transform: uppercase; font-weight: 400;
    line-height: 0.92; letter-spacing: 1px;
  }
  .card-back .wordmark {
    left: 30px; top: 22px; font-size: 46px; color: var(--maroon-deep);
  }
  .card-front .wordmark {
    right: 34px; bottom: 28px; font-size: 54px; text-align: right; color: var(--ink-red);
  }

  .back-content {
    position: absolute; left: 40px; top: 130px;
    font-size: 11.5px; line-height: 14.2px;
  }
  .section-title { text-transform: uppercase; margin-bottom: 6px; }
  .service-list, .affiliate-list { list-style: none; padding-left: 18px; }
  .affiliate-list { text-transform: uppercase; }
  .affiliates .section-title { margin-top: 12px; padding-left: 18px; }

  .front-content { position: absolute; left: 40px; top: 38px; }
  .person-name { font-size: 19px; font-weight: 600; }
  .person-title { font-size: 12px; margin-top: 2px; }
  .contact, .address, .registration {
    font-size: 13.5px; line-height: 17px; padding-left: 20px;
  }
  .contact { margin-top: 18px; }
  .address { margin-top: 14px; }
  .registration { margin-top: 14px; }
</style>
</head>
<body>
<main class="stage">
  <section class="card card-back" aria-label="Name card back">
    <div class="wordmark">Luminara<br>Ventures</div>
    <div class="back-content">
      <div class="services">
        <h2 class="section-title" style="font-size:11.5px;font-weight:400;">Our Core Services</h2>
        <ul class="service-list">
          <li>Incorporation services</li>
          <li>Corporate Secretarial Services</li>
          <li>Accountancy service</li>
          <li>Goods &amp; Services Taxation</li>
          <li>Corporate &amp; Personal Taxation</li>
          <li>Financial Reporting</li>
          <li>Payroll Administration</li>
        </ul>
      </div>
      <div class="affiliates">
        <h2 class="section-title" style="font-size:11.5px;font-weight:400;">Affiliates</h2>
        <ul class="affiliate-list">
          <li>Brightwave Corporate Services Pte Ltd</li>
          <li>Pinnacleformationspte Ltd</li>
          <li>Lim Management Services Pte Ltd</li>
          <li>RW Ho and Company Pte Ltd</li>
          <li>Ledgerly Academy</li>
        </ul>
      </div>
    </div>
  </section>

  <section class="card card-front" aria-label="Name card front">
    <div class="front-content">
      <h1 class="person-name">Tan Wei Ling CA (Singapore)</h1>
      <p class="person-title">Director</p>
      <p class="contact">
        Tel +65 6481 2957<br>
        Mobile +65 9172 3086<br>
        tan@luminaraventures.com.sg<br>
        www.luminaraventures.com.sg
      </p>
      <p class="address">
        47 Plover Lane, #07-12 Harbourlight Plaza<br>
        Singapore 276351
      </p>
      <p class="registration">Registration No. 208711845K</p>
    </div>
    <div class="wordmark">Luminara<br>Ventures</div>
  </section>
</main>
</body>
</html>
```